New Business Card Design Project

I would like to purchase a customized version of a design you have previously submitted - https://www.plorvexa.com/design/7314826<br/><br/>I would like to incorporate the attached Images for my fitness company "TrelmoKor Athletics". My initial services is personal training and athletic performance. I would like a card that has one a shiny black side with the silver logo and the side with a white background utilizing the gold logo. On the white side, put "Sports Performance and Functional Strength Training" under the logo.
Industry/Entity Type
Fitness
Contact Information for Business Card
Quillan Morrow
Owner and Trainer
555.271.9384
quillan.morrow@trelmokorathletics.com
Look and feel
Each slider illustrates characteristics of the customer's brand and the style your logo design should communicate.

```html
<!DOCTYPE html>
<html lang="en">
<head>
<meta charset="utf-8">
<title>TrelmoKor Athletics – Business Card</title>
<link rel="stylesheet" href="https://fonts.googleapis.com/css2?family=Lato:wght@400;700&display=swap">
<style>
  :root {
    --page-bg: #ebebea;
    --card-white: #ffffff;
    --card-black: #0d0d0d;
    --ink: #141414;
    --gold: #9a7b3c;
    --gold-light: #c7a862;
    --silver: #c9cacc;
    --card-w: 540px;
    --card-h: 309px;
  }
  * { box-sizing: border-box; margin: 0; padding: 0; }
  html, body { width: 1200px; height: 856px; overflow: hidden; }
  body {
    background: var(--page-bg);
    font-family: "Lato", Arial, sans-serif;
    color: var(--ink);
    display: flex;
    align-items: center;
    justify-content: center;
    gap: 48px;
  }
  .card {
    width: var(--card-w);
    height: var(--card-h);
    border-radius: 24px;
    position: relative;
    overflow: hidden;
    box-shadow: 0 6px 18px rgba(0,0,0,0.12);
  }
  .card-front { background: var(--card-white); }
  .card-back {
    background: var(--card-black);
    display: flex;
    align-items: center;
    justify-content: center;
  }

  .brand {
    display: flex;
    align-items: center;
    justify-content: center;
    gap: 9px;
    font-weight: 700;
    letter-spacing: 0.08em;
    text-transform: uppercase;
  }
  .brand-dot { border-radius: 50%; flex: none; }
  .brand-front { color: var(--gold); font-size: 15px; margin-top: 30px; }
  .brand-front .brand-dot { width: 34px; height: 34px; background: var(--gold); }
  .brand-back { color: var(--silver); font-size: 20px; }
  .brand-back .brand-dot { width: 48px; height: 48px; background: var(--silver); }

  .contact { text-align: center; margin-top: 22px; }
  .contact-name { font-size: 21px; font-weight: 700; line-height: 1; }
  .contact-title { font-size: 11px; margin-top: 4px; }
  .contact-stars { display: flex; justify-content: center; gap: 4px; margin-top: 5px; }
  .contact-phone { font-size: 38px; font-weight: 400; line-height: 1; margin-top: 10px; letter-spacing: 0.01em; }
  .contact-email { font-size: 13px; margin-top: 4px; }

  .tagline-band {
    position: absolute;
    left: 0; right: 0;
    bottom: 18px;
    height: 26px;
    background: linear-gradient(90deg, var(--gold) 0%, var(--gold-light) 50%, var(--gold) 100%);
    color: #fff;
    font-size: 12px;
    letter-spacing: 0.02em;
    display: flex;
    align-items: center;
    justify-content: center;
  }
  .tagline-band::before {
    content: "";
    position: absolute;
    left: 0; right: 0; top: -5px;
    height: 1px;
    background: var(--gold);
  }
</style>
</head>
<body>
  <section class="card card-front" aria-label="Card front">
    <div class="brand brand-front"><span class="brand-dot"></span>TrelmoKor Athletics</div>
    <div class="contact">
      <p class="contact-name">Quillan Morrow</p>
      <p class="contact-title">Owner and Trainer</p>
      <div class="contact-stars" aria-hidden="true">
        <svg width="42" height="9" viewBox="0 0 42 9">
          <g fill="#9a7b3c">
            <polygon points="4.5,0 5.6,3.3 9,3.3 6.2,5.3 7.3,8.6 4.5,6.6 1.7,8.6 2.8,5.3 0,3.3 3.4,3.3"/>
            <polygon transform="translate(16.5 0)" points="4.5,0 5.6,3.3 9,3.3 6.2,5.3 7.3,8.6 4.5,6.6 1.7,8.6 2.8,5.3 0,3.3 3.4,3.3"/>
            <polygon transform="translate(33 0)" points="4.5,0 5.6,3.3 9,3.3 6.2,5.3 7.3,8.6 4.5,6.6 1.7,8.6 2.8,5.3 0,3.3 3.4,3.3"/>
          </g>
        </svg>
      </div>
      <p class="contact-phone">555.271.9384</p>
      <p class="contact-email">quillan.morrow@trelmokorathletics.com</p>
    </div>
    <div class="tagline-band">Sports Performance and Functional Strength Training</div>
  </section>

  <section class="card card-back" aria-label="Card back">
    <div class="brand brand-back"><span class="brand-dot"></span>TrelmoKor Athletics</div>
  </section>
</body>
</html>
```